Business Card Design

I need a business card for company that is a limited company that was originally an off-road vehicle company (atv's side by sides snowmobiles and motorcycles) and I have recently sold the assets of the company that was operating under a different name and have become semi retired. I continue to do maintenance on these types of vehicles and also sell and install parts and accessories. Recently I have also contracted to a snowmobile club to operate their groomer to groom the snowmobile trails. I would like bright and bold colors.
Industry/Entity Type
Club
Contact Information for Business Card
KTV Holdings Ltd.
Milo Fenwick
780-413-2769

```html
<!DOCTYPE html>
<html lang="en">
<head>
<meta charset="utf-8">
<title>KTV Holdings Ltd. – Business Card</title>
<link href="https://fonts.googleapis.com/css2?family=Kurale&display=swap" rel="stylesheet">
<style>
  :root {
    --backdrop: #0a2a78;
    --card-yellow: #fff200;
    --card-black: #000000;
    --ink-black: #000000;
    --ink-yellow: #fff200;
  }
  html, body {
    margin: 0;
    padding: 0;
    width: 1200px;
    height: 1000px;
    overflow: hidden;
    background: var(--backdrop);
    font-family: "Kurale", serif;
  }
  .canvas {
    position: relative;
    width: 1200px;
    height: 1000px;
  }
  .card {
    position: absolute;
    top: 226px;
    width: 359px;
    height: 610px;
    border-radius: 14px;
    overflow: hidden;
  }
  .card--front { left: 230px; background: var(--card-yellow); }
  .card--back  { left: 610px; background: var(--card-black); border: 1px solid #555; box-sizing: border-box; }

  .accent-bar { position: absolute; background: var(--ink-black); width: 16px; }
  .accent-bar--top { left: 52px; top: 0; height: 162px; }
  .accent-bar--bottom { left: 291px; bottom: 0; height: 163px; }

  .company-name {
    position: absolute;
    left: 0;
    width: 100%;
    text-align: center;
    margin: 0;
    font-weight: 400;
    line-height: 1.05;
  }
  .card--front .company-name { top: 255px; font-size: 44px; color: var(--ink-black); }
  .card--back .company-name { top: 80px; font-size: 32px; color: var(--ink-yellow); }

  .rule {
    position: absolute;
    left: 0;
    top: 286px;
    width: 86px;
    height: 9px;
    background: var(--ink-yellow);
  }
  .person-name {
    position: absolute;
    left: 112px;
    top: 270px;
    margin: 0;
    font-size: 27px;
    font-weight: 400;
    color: var(--ink-yellow);
    white-space: nowrap;
  }
  .credentials {
    position: absolute;
    left: 0;
    top: 360px;
    width: 100%;
    margin: 0;
    padding: 0;
    list-style: none;
    text-align: center;
    font-size: 14px;
    line-height: 21px;
    color: var(--ink-yellow);
  }
  .contact {
    position: absolute;
    right: 14px;
    top: 522px;
    text-align: center;
    color: var(--ink-yellow);
    font-style: normal;
  }
  .contact__phone { display: block; font-size: 22px; line-height: 28px; }
  .contact__email { display: block; font-size: 20px; line-height: 26px; }
</style>
</head>
<body>
<main class="canvas">
  <section class="card card--front" aria-label="Card front">
    <span class="accent-bar accent-bar--top"></span>
    <h1 class="company-name">KTV<br>Holdings Ltd.</h1>
    <span class="accent-bar accent-bar--bottom"></span>
  </section>

  <section class="card card--back" aria-label="Card back">
    <h2 class="company-name">KTV<br>Holdings Ltd.</h2>
    <span class="rule"></span>
    <h3 class="person-name">Milo Fenwick</h3>
    <ul class="credentials">
      <li>Journeyman Red Seal Automotive Technician</li>
      <li>Journeyman Red Seal Motorcycle Technician</li>
      <li>Journeyman Parts Man</li>
    </ul>
    <address class="contact">
      <span class="contact__phone">780.413.2769</span>
      <span class="contact__email">ktvhold.77@mailbox.com</span>
    </address>
  </section>
</main>
</body>
</html>
```